For a German comparison website comparing the best online trading brokers I need 10 banners for Facebook advertising. The banners should be a size of 1200x628 with one of the following texts:
1) Traden für Anfänger
25 Euro gratis
2) Traden Sie online
25 Euro gratis
3) Online-Trading für Anfänger
4) Trading für Einsteiger
25 Euro gratis
5) Aktien für Einsteiger
25 Euro gratis
The targeted website is www.marvolink.ch and it compares brokers where traders can trade shares, commodities,indices and Forex.

```html
<!DOCTYPE html>
<html lang="de">
<head>
<meta charset="UTF-8">
<title>Aktien für Einsteiger – 25€ gratis</title>
<link href="https://fonts.googleapis.com/css2?family=Anton&family=Roboto:wght@700&display=swap" rel="stylesheet">
<style>
  :root {
    --navy: #1b2775;
    --red: #c9151b;
    --orange: #f26b10;
    --white: #ffffff;
    --desk-light: #f3f4f6;
    --desk-mid: #dde2e7;
    --screen-light: #3d5aa8;
    --screen-dark: #0f1d4d;
    --chart-blue: #3b7fc0;
    --arrow-red: #e0353a;
  }
  html, body {
    margin: 0;
    padding: 0;
    overflow: hidden;
    background: var(--white);
  }
  .banner {
    position: relative;
    width: 1200px;
    height: 628px;
    overflow: hidden;
    font-family: "Anton", "Impact", sans-serif;
  }
  .photo-meeting {
    position: absolute;
    inset: 0;
    background: linear-gradient(120deg, var(--desk-light) 0%, var(--desk-mid) 45%, #cfd6de 70%, var(--desk-light) 100%);
  }
  .photo-ticker {
    position: absolute;
    inset: 0;
    clip-path: polygon(760px 0, 1200px 0, 1200px 628px, 860px 628px);
    background: linear-gradient(200deg, var(--screen-light) 0%, #263f8a 45%, var(--screen-dark) 100%);
  }
  .scene-graphics {
    position: absolute;
    inset: 0;
  }
  .price {
    font-family: "Roboto", "Arial", sans-serif;
    font-weight: 700;
    fill: var(--white);
  }
  .price-faint { fill-opacity: 0.3; }
  .chart-sheet { fill: var(--white); fill-opacity: 0.92; }
  .chart-bar { fill: var(--chart-blue); }
  .chart-line { fill: #9fb7cf; }
  .down-arrow { fill: var(--arrow-red); }
  .headline {
    position: absolute;
    top: 4px;
    left: 0;
    width: 1200px;
    margin: 0;
    text-align: center;
    font-size: 82px;
    font-weight: 400;
    line-height: 1.05;
    letter-spacing: 5px;
    color: var(--navy);
    -webkit-text-stroke: 4px var(--white);
    paint-order: stroke fill;
  }
  .offer {
    position: absolute;
    left: 14px;
    bottom: 2px;
    margin: 0;
    font-size: 160px;
    line-height: 1;
    letter-spacing: 1px;
    -webkit-text-stroke: 7px var(--white);
    paint-order: stroke fill;
    white-space: nowrap;
  }
  .offer-amount { color: var(--red); }
  .offer-free { color: var(--orange); }
</style>
</head>
<body>
  <main class="banner">
    <div class="photo-meeting" role="img" aria-label="Business people at a desk pointing pens at printed bar charts"></div>
    <div class="photo-ticker" role="img" aria-label="Blue stock exchange screen listing share prices with red down arrows"></div>

    <svg class="scene-graphics" width="1200" height="628" viewBox="0 0 1200 628" aria-hidden="true">
      <g class="chart-printout" transform="rotate(-10 380 380)">
        <rect class="chart-sheet" x="220" y="250" width="330" height="240"/>
        <rect class="chart-line" x="245" y="272" width="180" height="8"/>
        <rect class="chart-line" x="245" y="288" width="120" height="6"/>
        <rect class="chart-bar" x="250" y="340" width="14" height="40"/>
        <rect class="chart-bar" x="270" y="325" width="14" height="55"/>
        <rect class="chart-bar" x="290" y="350" width="14" height="30"/>
        <rect class="chart-bar" x="310" y="315" width="14" height="65"/>
        <rect class="chart-bar" x="330" y="335" width="14" height="45"/>
        <rect class="chart-bar" x="380" y="330" width="12" height="50"/>
        <rect class="chart-bar" x="398" y="345" width="12" height="35"/>
        <rect class="chart-bar" x="416" y="320" width="12" height="60"/>
        <rect class="chart-bar" x="434" y="338" width="12" height="42"/>
        <rect class="chart-bar" x="452" y="312" width="12" height="68"/>
        <rect class="chart-bar" x="470" y="328" width="12" height="52"/>
        <rect class="chart-bar" x="260" y="410" width="10" height="50"/>
        <rect class="chart-bar" x="276" y="425" width="10" height="35"/>
        <rect class="chart-bar" x="292" y="400" width="10" height="60"/>
        <rect class="chart-bar" x="308" y="418" width="10" height="42"/>
        <rect class="chart-bar" x="324" y="405" width="10" height="55"/>
        <rect class="chart-bar" x="340" y="420" width="10" height="40"/>
        <rect class="chart-bar" x="356" y="398" width="10" height="62"/>
        <rect class="chart-bar" x="372" y="415" width="10" height="45"/>
      </g>

      <g class="ticker-prices">
        <text class="price price-faint" x="770" y="170" font-size="88" transform="rotate(-14 770 170)">$0.90</text>
        <text class="price" x="788" y="292" font-size="98" transform="rotate(-14 788 292)">$1.01</text>
        <text class="price" x="848" y="385" font-size="90" transform="rotate(-14 848 385)">$3.09</text>
        <text class="price" x="902" y="455" font-size="78" transform="rotate(-14 902 455)">$0.19</text>
        <text class="price" x="946" y="515" font-size="68" transform="rotate(-14 946 515)">$0.72</text>
        <text class="price" x="980" y="562" font-size="60" transform="rotate(-14 980 562)">$5.49</text>
        <text class="price" x="996" y="602" font-size="54" transform="rotate(-14 996 602)">$0.95</text>
        <text class="price" x="1012" y="640" font-size="50" transform="rotate(-14 1012 640)">$0.41</text>
      </g>

      <g class="ticker-arrows">
        <polygon class="down-arrow" points="1095,0 1200,0 1200,60 1160,75"/>
        <polygon class="down-arrow" points="1128,130 1200,115 1200,185 1175,195"/>
        <polygon class="down-arrow" points="1155,245 1200,236 1200,285 1188,290"/>
        <polygon class="down-arrow" points="1178,335 1200,330 1200,360"/>
      </g>
    </svg>

    <h1 class="headline">AKTIEN FÜR EINSTEIGER</h1>
    <p class="offer"><span class="offer-amount">25€</span><span class="offer-free">GRATIS</span></p>
  </main>
</body>
</html>
```